TOR Capital Allies LLC a High Risk Big Rewards company for Rich Young Entrepreneurs

We would like a very modern, powerful in the eyes of our customers, modern, minimalist feel, financial gain. this business card is for young Rich entrepreneurs who want to invest money into High Risk, Big Rewards Businesses. The card Should sell the business!! let your creativity go Wild! I pick most of the designers for this project because of your BOLD Designs, I would like this card to be Bold, Modern, Minimalist, use as many effects in your graphic Artist Mind, Do not let the Financial sound of this business to make you think Conservative that's the last thing we are! if you have a lot of money and you want to play a risky market call US
Updates

Project Deadline Extended
Reason: have not received, enough designs to choose 1st and second place, sure I have received over 100 designs but it seems most designers are submitting every card they have ever made before and calling it mine, please we are looking for fresh ideas please!

Target Market(s)

Private Risky Investors

Industry/Entity Type

Financial

Contact Information for Business Card

powerful in the eyes of our customers,modern, minimalist feel

Font styles to use
Other font styles liked:
• Modern feeling fonts

Requirements
Must have
• The Company Name is TOR Capital Allies LLC and it must be on the CARD
• My Name, title, Cell , email
• Dalton Fairweather G.E.D.
• Managing Member
• 404.658.1937
• dalton@torcapitalallies.example
Nice to have
• try a black thick plastic card with round corners with Dalton Fairweather GED (make sure GED is smaller than name) just on one side of the card, and my phone number with out the icons and email on the other side, this card should look like a exclusive credit card or exclusive VIP card, something you would never loose

```html
<!DOCTYPE html>
<html lang="en">
<head>
<meta charset="utf-8">
<title>TOR Capital Allies LLC — Business Card</title>
<link rel="stylesheet" href="https://fonts.googleapis.com/css2?family=Archivo+Narrow:wght@400&family=Raleway:wght@300;400&display=swap">
<style>
  :root {
    --page-bg: #ffffff;
    --card-bg: #000000;
    --text-primary: #ffffff;
    --text-muted: #868c94;
    --monogram: #1e262d;
    --card-shadow: rgba(0, 0, 0, 0.55);
  }
  * { margin: 0; padding: 0; box-sizing: border-box; }
  html, body {
    width: 1200px;
    height: 1000px;
    overflow: hidden;
    background: var(--page-bg);
  }
  .canvas {
    position: relative;
    width: 1200px;
    height: 1000px;
  }
  .card {
    position: absolute;
    left: 338px;
    width: 533px;
    height: 320px;
    border-radius: 36px;
    background: var(--card-bg);
    box-shadow: 0 6px 14px var(--card-shadow);
    overflow: hidden;
  }
  .card--front { top: 146px; }
  .card--back { top: 522px; }

  .company-name {
    position: absolute;
    left: 32px;
    top: 252px;
    font-family: "Raleway", sans-serif;
    font-weight: 400;
    font-size: 32px;
    color: var(--text-primary);
    white-space: nowrap;
  }

  .contact {
    position: absolute;
    left: 35px;
    top: 30px;
    font-family: "Archivo Narrow", sans-serif;
  }
  .contact__name {
    font-size: 23px;
    line-height: 30px;
    color: var(--text-primary);
  }
  .contact__credential {
    font-size: 17px;
  }
  .contact__title {
    font-size: 19px;
    line-height: 24px;
    color: var(--text-muted);
  }
  .contact__details {
    margin-top: 18px;
    font-size: 16px;
    line-height: 25px;
    letter-spacing: 0.6px;
    color: var(--text-muted);
  }

  .monogram {
    position: absolute;
    right: 32px;
    bottom: 10px;
    font-family: "Raleway", sans-serif;
    font-weight: 300;
    font-size: 128px;
    line-height: 1;
    color: var(--monogram);
    white-space: nowrap;
  }
</style>
</head>
<body>
  <main class="canvas">
    <section class="card card--front" aria-label="Card front">
      <p class="company-name">TOR Capital Allies LLC</p>
    </section>

    <section class="card card--back" aria-label="Card back">
      <div class="contact">
        <p class="contact__name">Dalton Fairweather <span class="contact__credential">G.E.D.</span></p>
        <p class="contact__title">Managing Member</p>
        <div class="contact__details">
          <p class="contact__email">dalton@torcapitalallies.example</p>
          <p class="contact__phone">404.658.1937</p>
        </div>
      </div>
      <p class="monogram">TOR</p>
    </section>
  </main>
</body>
</html>
```